Elevating our current Business Card Design

We want to elevate our current business card with a new design to look like a marlow 800 company. We are a premium lubricant distributor (oil and grease).
We need 2 versions, version 1 is as per the uploaded a copy of our current business card with the English version.
For our Chinese version we need to use the front to be English in English and have the back of the card designed exactly like the front for all info to be in Chinese.
The design template needs to be such that we can amend the template with adding different information for each person's card.
The background colour of the card can be changed- we just need to clearly see all information on the card and logos.
The TRV and Verdant Mark logos cannot have any colour or display changes- only use the logos attached.
All logos need to be included and all information from the attached current card

```html
<!DOCTYPE html>
<html lang="en">
<head>
<meta charset="utf-8">
<title>Meridian Lube Traders – Business Cards</title>
<link rel="stylesheet" href="https://fonts.googleapis.com/css2?family=Poppins:wght@400;500;600;700;800&family=Noto+Sans+TC:wght@400;500&display=swap">
<style>
  :root{
    --red:#e3261f;
    --ink:#2b2b2b;
    --card-top:#fbfbfb;
    --card-bottom:#ececec;
    --stage:#e4e4e4;
    --badge-fill:#d6d6d6;
  }
  *{box-sizing:border-box;margin:0;padding:0}
  html,body{width:1200px;height:2400px;overflow:hidden}
  body{background:var(--stage);font-family:"Poppins",sans-serif;color:var(--ink);position:relative}

  .card{position:absolute;left:100px;width:1000px;height:610px;
    background:linear-gradient(160deg,var(--card-top),var(--card-bottom));
    box-shadow:0 14px 34px rgba(0,0,0,.16);overflow:hidden}
  .card--english{top:110px}
  .card--chinese{top:885px}
  .card--back{top:1660px}

  .logo-box{position:absolute;left:60px;top:0;width:340px;height:240px;background:#fff;
    border:3px solid var(--red);border-top:none;border-radius:0 0 32px 32px;
    display:flex;align-items:center;justify-content:center;gap:14px}
  .brand-dot{width:26px;height:26px;border-radius:50%;background:var(--red)}
  .brand-name{font-weight:800;font-size:82px;color:var(--red);letter-spacing:2px;line-height:1}

  .address{position:absolute;left:66px;top:262px;font-size:19px;line-height:1.3;color:var(--ink);display:flex;gap:10px}
  .address svg{flex:none;margin-top:3px}
  .card--chinese .address{font-family:"Noto Sans TC","Poppins",sans-serif}

  .partner-strip{position:absolute;left:40px;top:380px;width:470px;height:72px;display:flex}
  .strip-brand{width:240px;background:#fff;border:3px solid var(--red);border-right:none;
    display:flex;align-items:center;gap:10px;padding-left:14px}
  .strip-brand .brand-name{font-size:30px}
  .strip-brand .brand-sub{font-size:9px;font-weight:600;color:var(--red);line-height:1.15;text-transform:uppercase}
  .strip-partner{flex:1;background:var(--red);color:#fff;display:flex;flex-direction:column;justify-content:center;
    padding-left:22px;clip-path:polygon(0 0,100% 0,92% 100%,0 100%)}
  .strip-partner .partner-name{font-weight:800;font-size:28px;line-height:1;letter-spacing:1px}
  .strip-partner .partner-sub{font-size:11px;font-weight:500;letter-spacing:1px;margin-top:3px}

  .person{position:absolute;left:585px;top:150px;width:390px}
  .person-name{font-size:40px;font-weight:800;letter-spacing:1px;line-height:1}
  .person-name .first{color:var(--red)}
  .person-name .last{color:var(--ink)}
  .person-title{font-size:19px;color:var(--ink);margin-top:6px}
  .card--chinese .person-name{font-family:"Noto Sans TC",sans-serif;font-weight:500;color:var(--red);font-size:40px}
  .card--chinese .person-title{font-family:"Noto Sans TC",sans-serif;font-size:18px}
  .person-rule{width:200px;height:3px;background:var(--red);margin:14px 0 16px}
  .contact-list{list-style:none;font-size:18px;line-height:1.5}
  .contact-list li{display:flex;align-items:center;gap:12px}
  .contact-list svg{flex:none}

  .badges{position:absolute;left:600px;top:445px;display:flex;gap:60px;align-items:center}
  .badge{display:block;background:var(--badge-fill)}
  .badge--member{width:120px;height:90px;border-radius:10px}
  .badge--cert{width:100px;height:100px;border-radius:50%}

  .edge{position:absolute;background:var(--red)}
  .edge--left{left:0;top:70px;width:90px;height:300px;clip-path:polygon(0 10%,100% 0,55% 100%,0 100%)}
  .edge--right{right:0;top:230px;width:90px;height:300px;clip-path:polygon(45% 0,100% 0,100% 100%,0 90%)}
  .back-lockup{position:absolute;left:0;right:0;top:190px;display:flex;align-items:center;justify-content:center;gap:28px}
  .back-lockup .brand-name{font-size:110px}
  .back-lockup .brand-dot{width:34px;height:34px}
  .back-company{font-size:30px;font-weight:500;color:var(--red);line-height:1.15;text-transform:uppercase}
  .back-rule{position:absolute;left:400px;top:430px;width:200px;height:3px;background:var(--red)}
  .back-web{position:absolute;left:0;right:0;top:455px;text-align:center;font-size:26px;color:var(--ink)}
</style>
</head>
<body>

<section class="card card--english">
  <div class="logo-box"><span class="brand-dot"></span><span class="brand-name">MLT</span></div>
  <p class="address">
    <svg width="16" height="22" viewBox="0 0 16 22"><path d="M8 0a8 8 0 0 1 8 8c0 6-8 14-8 14S0 14 0 8a8 8 0 0 1 8-8z" fill="var(--red)"/><circle cx="8" cy="8" r="3" fill="#fff"/></svg>
    <span>48 Harbour Freight Way<br>Eastdale WA 6100</span>
  </p>
  <div class="partner-strip">
    <div class="strip-brand"><span class="brand-name">MLT</span><span class="brand-sub">Meridian<br>Lube<br>Traders</span></div>
    <div class="strip-partner"><span class="partner-name">CORVANE</span><span class="partner-sub">PREMIUM LUBRICANTS</span></div>
  </div>
  <div class="person">
    <h1 class="person-name"><span class="first">MARA</span> <span class="last">QUINLAN</span></h1>
    <p class="person-title">Administration Executive</p>
    <div class="person-rule"></div>
    <ul class="contact-list">
      <li><svg width="18" height="18" viewBox="0 0 18 18"><path d="M3 2h4l1 4-2 1a10 10 0 0 0 5 5l1-2 4 1v4a2 2 0 0 1-2 2A14 14 0 0 1 1 4a2 2 0 0 1 2-2z" fill="var(--red)"/></svg>1300 000 111</li>
      <li><svg width="18" height="18" viewBox="0 0 18 18"><rect x="4" y="1" width="10" height="16" rx="2" fill="none" stroke="var(--red)" stroke-width="2"/></svg>+61 400 000 123</li>
      <li><svg width="18" height="18" viewBox="0 0 18 18"><rect x="4" y="1" width="10" height="5" fill="var(--red)"/><rect x="1" y="6" width="16" height="8" rx="2" fill="var(--red)"/><rect x="5" y="11" width="8" height="6" fill="#fff" stroke="var(--red)" stroke-width="1.5"/></svg>+61 8 9000 4455</li>
      <li><svg width="18" height="18" viewBox="0 0 18 18"><rect x="1" y="3" width="16" height="12" fill="var(--red)"/><path d="M1 3l8 7 8-7" fill="none" stroke="#fff" stroke-width="1.5"/></svg>mara.quinlan@meridianlube.com</li>
      <li><svg width="18" height="18" viewBox="0 0 18 18"><circle cx="9" cy="9" r="8" fill="none" stroke="var(--red)" stroke-width="1.6"/><ellipse cx="9" cy="9" rx="3.5" ry="8" fill="none" stroke="var(--red)" stroke-width="1.3"/><path d="M1 9h16M2.5 5h13M2.5 13h13" stroke="var(--red)" stroke-width="1.2"/></svg>www.meridianlube.com</li>
    </ul>
  </div>
  <div class="badges">
    <span class="badge badge--member" role="img" aria-label="Verdant Mark network member badge"></span>
    <span class="badge badge--cert" role="img" aria-label="TRV system certification badge"></span>
  </div>
</section>

<section class="card card--chinese" lang="zh-Hant">
  <div class="logo-box"><span class="brand-dot"></span><span class="brand-name">MLT</span></div>
  <p class="address">
    <svg width="16" height="22" viewBox="0 0 16 22"><path d="M8 0a8 8 0 0 1 8 8c0 6-8 14-8 14S0 14 0 8a8 8 0 0 1 8-8z" fill="var(--red)"/><circle cx="8" cy="8" r="3" fill="#fff"/></svg>
    <span>48 港口貨運路東代爾,<br>WA 6100</span>
  </p>
  <div class="partner-strip">
    <div class="strip-brand"><span class="brand-name">MLT</span><span class="brand-sub">Meridian<br>Lube<br>Traders</span></div>
    <div class="strip-partner"><span class="partner-name">CORVANE</span><span class="partner-sub">PREMIUM LUBRICANTS</span></div>
  </div>
  <div class="person">
    <h1 class="person-name">瑪拉·昆蘭</h1>
    <p class="person-title">行政主管</p>
    <div class="person-rule"></div>
    <ul class="contact-list">
      <li><svg width="18" height="18" viewBox="0 0 18 18"><path d="M3 2h4l1 4-2 1a10 10 0 0 0 5 5l1-2 4 1v4a2 2 0 0 1-2 2A14 14 0 0 1 1 4a2 2 0 0 1 2-2z" fill="var(--red)"/></svg>1300 000 111</li>
      <li><svg width="18" height="18" viewBox="0 0 18 18"><rect x="4" y="1" width="10" height="16" rx="2" fill="none" stroke="var(--red)" stroke-width="2"/></svg>+61 400 000 123</li>
      <li><svg width="18" height="18" viewBox="0 0 18 18"><rect x="4" y="1" width="10" height="5" fill="var(--red)"/><rect x="1" y="6" width="16" height="8" rx="2" fill="var(--red)"/><rect x="5" y="11" width="8" height="6" fill="#fff" stroke="var(--red)" stroke-width="1.5"/></svg>+61 8 9000 4455</li>
      <li><svg width="18" height="18" viewBox="0 0 18 18"><rect x="1" y="3" width="16" height="12" fill="var(--red)"/><path d="M1 3l8 7 8-7" fill="none" stroke="#fff" stroke-width="1.5"/></svg>mara.quinlan@meridianlube.com</li>
      <li><svg width="18" height="18" viewBox="0 0 18 18"><circle cx="9" cy="9" r="8" fill="none" stroke="var(--red)" stroke-width="1.6"/><ellipse cx="9" cy="9" rx="3.5" ry="8" fill="none" stroke="var(--red)" stroke-width="1.3"/><path d="M1 9h16M2.5 5h13M2.5 13h13" stroke="var(--red)" stroke-width="1.2"/></svg>www.meridianlube.com</li>
    </ul>
  </div>
  <div class="badges">
    <span class="badge badge--member" role="img" aria-label="Verdant Mark network member badge"></span>
    <span class="badge badge--cert" role="img" aria-label="TRV system certification badge"></span>
  </div>
</section>

<section class="card card--back">
  <div class="edge edge--left"></div>
  <div class="edge edge--right"></div>
  <div class="back-lockup">
    <span class="brand-dot"></span><span class="brand-name">MLT</span>
    <p class="back-company">Meridian<br>Lube<br>Traders</p>
  </div>
  <div class="back-rule"></div>
  <p class="back-web">www.meridianlube.com</p>
</section>

</body>
</html>
```